Business Card Design Project

New Business Card design for Varodine Technology Ltd using new Logo and new Tagline for staffing company.

About us from our website - www.varodine.example:

VaroDine is a leading and recognized Electronic Entertainment, Workforce Augmentation, and Project Management solutions provider with clients in Electronic Entertainment, Legal, Technology, Government and other verticals that range in size from start up organizations to Zenlar 500 companies. VaroDine is certified as an 8(a) minority and woman owned enterprise, established in 1998.

Target Market(s)

Companies in Electronic Entertainment, Legal, Government and Technology

Industry/Entity Type

Business

Requirements
Must have
• Must include in small letters the following information on back:

Established in 1998
8(a)(w)(e), Cage #7KRT9, DUNS #462137580

Front should have the following:
Derek Holloway
Vice President
5820 Birchmont Road
Fallowby, FB 482917
555-318-2746 X 100
555-902-6613 Fax
555-318-2746 Toll Free
name@varodine.example

Our Tagline: Connect • Collaborate • Achieve

```html
<!DOCTYPE html>
<html lang="en">
<head>
<meta charset="utf-8">
<title>VaroDine Business Cards</title>
<link rel="stylesheet" href="https://fonts.googleapis.com/css2?family=Open+Sans:wght@400;600;700&display=swap">
<style>
  :root {
    --page: #ffffff;
    --ink-dark: #121416;
    --ink-dark-strip: #1b1d1f;
    --silver-light: #c4c4c4;
    --silver-mid: #b3b3b3;
    --silver-strip: #3a3b3c;
    --brand-blue: #2f6fe0;
    --logo-light: #bfbfbf;
    --logo-dark: #4a5257;
    --text-light: #ffffff;
    --text-muted: #a9a9a9;
    --text-dark: #2b2f32;
  }
  * { box-sizing: border-box; margin: 0; padding: 0; }
  html, body { width: 1200px; height: 900px; overflow: hidden; background: var(--page); }
  body { position: relative; font-family: "Open Sans", Arial, sans-serif; }

  .card { position: absolute; width: 546px; height: 343px; overflow: hidden; }
  .card--dark { background: var(--ink-dark); color: var(--text-light); }
  .card--silver { background: linear-gradient(160deg, var(--silver-light), var(--silver-mid) 60%, #bdbdbd); color: var(--text-dark); }

  .pos-front-dark { left: 29px; top: 73px; }
  .pos-front-silver { left: 624px; top: 73px; }
  .pos-back-dark { left: 29px; top: 473px; }
  .pos-back-silver { left: 624px; top: 473px; }

  /* Fronts */
  .wordmark { position: absolute; left: 0; right: 0; top: 118px; text-align: center; font-weight: 600; font-size: 92px; line-height: 1; letter-spacing: -1px; }
  .card--dark .wordmark { color: var(--logo-light); }
  .card--silver .wordmark { color: var(--logo-dark); }
  .brand-dot { position: absolute; width: 26px; height: 26px; border-radius: 50%; background: var(--brand-blue); left: 259px; top: 70px; }
  .tagline { position: absolute; left: 0; right: 0; top: 243px; text-align: center; font-size: 22px; }
  .card--dark .tagline { color: var(--text-muted); }
  .card--silver .tagline { color: var(--text-dark); }

  .front-strip { position: absolute; left: 0; right: 0; bottom: 0; height: 38px; }
  .card--dark .front-strip { background: var(--ink-dark-strip); }
  .card--silver .front-strip { background: var(--silver-strip); }
  .front-strip__web { position: absolute; left: 10px; bottom: 8px; font-size: 10px; color: #d0d0d0; }
  .front-credentials { position: absolute; right: 10px; bottom: 8px; text-align: right; font-size: 10px; line-height: 1.35; }
  .card--dark .front-credentials { color: #d0d0d0; }
  .card--silver .front-credentials { color: #e8e8e8; }
  .card--silver .front-credentials__est { color: var(--text-dark); }

  /* Backs */
  .back-header { position: absolute; right: 36px; top: 26px; text-align: right; }
  .card--silver .back-band { position: absolute; left: 0; right: 0; top: 0; height: 87px; background: var(--silver-strip); }
  .person-name { font-weight: 700; font-size: 29px; line-height: 1.15; }
  .person-title { font-size: 15px; }
  .card--silver .back-header { color: var(--text-light); }

  .contact { position: absolute; right: 36px; text-align: right; font-size: 21px; line-height: 31px; }
  .contact--address { top: 105px; }
  .contact--lines { top: 180px; }
  .contact b { font-weight: 700; }

  .back-logo { position: absolute; left: 22px; top: 250px; display: flex; align-items: center; gap: 6px; font-weight: 600; font-size: 27px; }
  .back-logo__dot { width: 12px; height: 12px; border-radius: 50%; background: var(--brand-blue); }
  .card--dark .back-logo { color: var(--text-light); }
  .card--silver .back-logo { color: var(--logo-dark); }
  .back-web { position: absolute; left: 48px; top: 309px; font-size: 10px; }
  .card--dark .back-web { color: #cfcfcf; }
  .card--silver .back-web { color: var(--text-dark); }
</style>
</head>
<body>

<section class="card card--dark pos-front-dark">
  <span class="brand-dot"></span>
  <div class="wordmark">VaroDine</div>
  <p class="tagline">Connect • Collaborate • Achieve</p>
  <div class="front-strip">
    <span class="front-strip__web">www.varodine.example</span>
    <p class="front-credentials"><span class="front-credentials__est">Established in 1998</span><br>8(a)(w)(e), Cage #7KRT9, DUNS #462137580</p>
  </div>
</section>

<section class="card card--silver pos-front-silver">
  <span class="brand-dot"></span>
  <div class="wordmark">VaroDine</div>
  <p class="tagline">Connect • Collaborate • Achieve</p>
  <div class="front-strip">
    <span class="front-strip__web">www.varodine.example</span>
    <p class="front-credentials"><span class="front-credentials__est">Established in 1998</span><br>8(a)(w)(e), Cage #7KRT9, DUNS #462137580</p>
  </div>
</section>

<section class="card card--dark pos-back-dark">
  <div class="back-header">
    <p class="person-name">Derek Holloway</p>
    <p class="person-title">Vice President</p>
  </div>
  <p class="contact contact--address">5820 Birchmont Road<br>Fallowby, FB 482917</p>
  <p class="contact contact--lines">555-318-2746 X 100<br>555-902-6613 <b>fax</b><br>555-318-2746 <b>toll Free</b><br>name@varodine.example</p>
  <div class="back-logo"><span class="back-logo__dot"></span>VaroDine</div>
  <span class="back-web">www.varodine.example</span>
</section>

<section class="card card--silver pos-back-silver">
  <div class="back-band"></div>
  <div class="back-header">
    <p class="person-name">Derek Holloway</p>
    <p class="person-title">Vice President</p>
  </div>
  <p class="contact contact--address">5820 Birchmont Road<br>Fallowby, FB 482917</p>
  <p class="contact contact--lines">555-318-2746 X 100<br>555-902-6613 <b>fax</b><br>555-318-2746 <b>toll free</b><br>name@varodine.example</p>
  <div class="back-logo"><span class="back-logo__dot"></span>VaroDine</div>
  <span class="back-web">www.varodine.example</span>
</section>

</body>
</html>
```